IT Company, Needs new Logo and Letterhead Design

We need a Letterhead and possible a new logo for an existing IT Company. We are not happy with our current Letterhead that we are using in our quotes etc. We are happy to change our logo if required. We will upload our current logo and letterhead and look forward to getting some examples. We provide Server, Workstation and network support.

Target Market(s)

Small to Medium Sized Businesses.

Industry/Entity Type

It Company

Requirements
Must have
• Ability to edit the letterhead at a later date. Will need the source files for editing once approved.
Nice to have
• Same colour scheme, but we are open to suggestions.

```html
<!DOCTYPE html>
<html lang="en">
<head>
<meta charset="utf-8">
<title>Halden Network Services – Letterhead</title>
<link href="https://fonts.googleapis.com/css2?family=Questrial&display=swap" rel="stylesheet">
<style>
  :root {
    --navy: #1a2a54;
    --brand-blue: #1d3a78;
    --band-text: #c3c8d6;
    --paper: #ffffff;
  }
  html, body {
    margin: 0;
    padding: 0;
    overflow: hidden;
    background: var(--paper);
  }
  .letterhead {
    position: relative;
    width: 927px;
    height: 1200px;
    background: var(--paper);
    overflow: hidden;
    font-family: "Questrial", sans-serif;
  }
  .brand {
    position: absolute;
    left: 57px;
    top: 26px;
    display: flex;
    align-items: flex-end;
    gap: 26px;
  }
  .brand-name {
    margin: 0;
    font-family: "Questrial", sans-serif;
    font-weight: 400;
    font-size: 44px;
    line-height: 48px;
    letter-spacing: -0.5px;
    color: var(--brand-blue);
  }
  .brand-mark {
    display: block;
    margin-bottom: 6px;
  }
  .contact-band {
    position: absolute;
    left: 731px;
    top: 0;
    width: 196px;
    height: 1200px;
    background: var(--navy);
  }
  .contact-block {
    position: absolute;
    left: 22px;
    margin: 0;
    font-style: normal;
    font-family: "Questrial", sans-serif;
    font-size: 10.5px;
    line-height: 15.2px;
    color: var(--band-text);
    white-space: nowrap;
  }
  .contact-address { top: 106px; }
  .contact-phones { top: 210px; }
  .contact-block span { display: block; }
</style>
</head>
<body>
  <main class="letterhead">
    <header class="brand">
      <h1 class="brand-name">Halden Network<br>Services</h1>
      <svg class="brand-mark" width="26" height="26" viewBox="0 0 26 26" aria-hidden="true">
        <circle cx="13" cy="13" r="12" fill="var(--brand-blue)"/>
      </svg>
    </header>

    <aside class="contact-band">
      <address class="contact-block contact-address">
        <span>PO Box 2841,</span>
        <span>Coral Arcade, QLD 4571,</span>
        <span>9 Tamber Street Kawana Heights</span>
        <span>72 Larkin Road, Ashgrove</span>
      </address>
      <p class="contact-block contact-phones">
        <span>PHONE: 1300 482 615</span>
        <span>MOB: 0412 907 368</span>
      </p>
    </aside>
  </main>
</body>
</html>
```